Mr. Kelpfin Restaurant Menu Design

I would like for you to please create a menu design for my seafood restaurant called Mr. Kelpfin. I uploaded the logo of my restaurant and would like the same colors and font to be used on the menu. The headings of my menu should include the following:
What's your catch?
What's your sauce?
How "Hot" can you go?
Medium?
Mild?
Wild?
Soups
Paella
Katsu
Add Ons
Sweet Cravings
Thirsty?
It would be nice to see something creative and simple preferably one page.
I already uploaded my logo on the brief section.
Thank you.
Target Market(s)
Family friendly
Industry/Entity Type
Seafood Restaurant
Look and feel

```html
<!DOCTYPE html>
<html lang="en">
<head>
<meta charset="utf-8">
<title>Mr. Kelpfin Restaurant Menu</title>
<link rel="stylesheet" href="https://fonts.googleapis.com/css2?family=Fredoka:wght@600;700&display=swap">
<style>
  :root {
    --frame-light: #d9d9d9;
    --frame-dark: #8a8a8a;
    --frame-line: #3a3a3a;
    --paper: #ebfdfe;
    --band: #c68410;
    --heading-blue: #17a2e6;
    --title-white: #f7f3f0;
    --title-orange: #c97d10;
    --title-shadow: rgba(60, 40, 20, 0.55);
  }
  html, body {
    margin: 0;
    padding: 0;
    overflow: hidden;
  }
  body {
    width: 848px;
    height: 1200px;
  }
  .menu {
    position: relative;
    width: 848px;
    height: 1200px;
    overflow: hidden;
    font-family: "Fredoka", sans-serif;
  }
  .menu__frame {
    position: absolute;
    inset: 0;
    background:
      repeating-linear-gradient(45deg, var(--frame-light) 0 3px, var(--frame-dark) 3px 5px),
      var(--frame-light);
  }
  .menu__page {
    position: absolute;
    left: 36px;
    top: 30px;
    width: 779px;
    height: 1137px;
    background: var(--paper);
    border: 2px solid var(--frame-line);
    box-sizing: border-box;
  }
  .menu__band {
    position: absolute;
    left: 605px;
    top: 0;
    width: 172px;
    height: 100%;
    background: var(--band);
  }
  .menu__title {
    position: absolute;
    left: 58px;
    top: 18px;
    margin: 0;
    font-weight: 700;
    font-size: 100px;
    line-height: 1;
    letter-spacing: 3px;
    color: var(--title-white);
    -webkit-text-stroke: 10px var(--title-orange);
    paint-order: stroke fill;
    text-shadow: 6px 8px 6px var(--title-shadow);
  }
  .brand__mark {
    position: absolute;
    left: 512px;
    top: 42px;
  }
  .brand__name {
    position: absolute;
    left: 0;
    top: 244px;
    width: 598px;
    text-align: right;
    font-weight: 700;
    font-size: 36px;
    line-height: 1;
    color: var(--heading-blue);
    white-space: nowrap;
  }
  .sections {
    list-style: none;
    margin: 0;
    padding: 0;
  }
  .sections__item {
    position: absolute;
    left: 55px;
    font-weight: 700;
    font-size: 33px;
    line-height: 1;
    color: var(--heading-blue);
    white-space: nowrap;
  }
</style>
</head>
<body>
<main class="menu">
  <div class="menu__frame" role="img" aria-label="Decorative woven metallic border pattern"></div>
  <section class="menu__page">
    <div class="menu__band"></div>
    <h1 class="menu__title">MENU</h1>
    <svg class="brand__mark" width="192" height="192" viewBox="0 0 192 192" aria-hidden="true">
      <circle cx="96" cy="96" r="95" fill="#17a2e6"/>
    </svg>
    <span class="brand__name">Mr. Kelpfin</span>
    <ul class="sections">
      <li class="sections__item" style="top:182px">What's your catch?</li>
      <li class="sections__item" style="top:270px">What's your sauce?</li>
      <li class="sections__item" style="top:350px">How "Hot" can you go?</li>
      <li class="sections__item" style="top:436px">Mild?</li>
      <li class="sections__item" style="top:512px">Wild?</li>
      <li class="sections__item" style="top:594px">Medium?</li>
      <li class="sections__item" style="top:670px">Paella</li>
      <li class="sections__item" style="top:747px">Katsu</li>
      <li class="sections__item" style="top:829px">Add Ons</li>
      <li class="sections__item" style="top:914px">Soups</li>
      <li class="sections__item" style="top:991px">Sweet Cravings</li>
      <li class="sections__item" style="top:1072px">Thirsty?</li>
    </ul>
  </section>
</main>
</body>
</html>
```